Brightmoor Academy - Personal Development business 2.0 needs a social post format design.

https://www.brightmooracademy.example

Our focus with Brightmoor Academy is on developing people through knowledge and skills to improve their everyday lives.
We love simplicity, Quorel design and less is more.

We are crazy about personal growth, science, design, the latest gadgets and people.

We need 4 formats for our social media posts.
1. Blogs -to pronounce a blog post
2. Workshop /training - to pronounce our workshops/trainings (both online and offline)
3. Podcast - called "Wissel je blik". To pronounce a guest we've spoken. The host is called Berend.
4. Facts - to pronounce short facts about personal development. Invites people to read more.
The formats should include: high quality pictogram (better than the uploaded picto's), 1 of the 3 logo's in the design.
It's important that we can edit the design in Lumora Draw / Lumora Pixel to adjust the text in the format.

Attached you find four of our current designs, which are a poor example of how the designs should look like. These are just to show you how much lines of text (more or less) will be in the designs. So please do not make a design that looks like these ;) You have carte blanche.

Our customers are mostly women (80%). We focus on both business and casual customers.

Target Market(s)

80% woman, 20% men. We focus on both business and casual customers.

Requirements
Must have
• Less is more. Quorel Design alike. Simplicity.
Aimed at the women target audience.
Designs must be edible for adjusting the text in the format.
Nice to have
• Unique concept.
The design should "breathe".
Each design can have a different color, so customers identify the specific post with specific information. For example, blog is red, workshop post black, etc.

```html
<!DOCTYPE html>
<html lang="nl">
<head>
<meta charset="utf-8">
<title>Brightmoor Academy – social posts</title>
<link href="https://fonts.googleapis.com/css2?family=Montserrat:wght@400;500;600&display=swap" rel="stylesheet">
<style>
  :root {
    --stage: #767676;
    --paper: #e3e2df;
    --white: #ffffff;
    --kraft: #8a5a2c;
    --ink: #1b1b1b;
    --red: #e41e2b;
  }
  * { margin: 0; padding: 0; box-sizing: border-box; }
  html, body {
    width: 1200px; height: 666px; overflow: hidden;
    background: var(--stage);
    font-family: 'Montserrat', Arial, sans-serif;
  }
  .post {
    position: absolute; top: 70px;
    width: 493px; height: 493px;
    background: var(--paper);
    overflow: hidden;
  }
  .post--blog { left: 73px; }
  .post--podcast { left: 634px; }

  .post__photo {
    position: absolute; left: 76px; top: 59px;
    width: 334px; height: 363px;
  }
  .post--blog .post__photo {
    background: linear-gradient(150deg, #f1ece3 0%, #e2d9c8 40%, #a89068 68%, #ece6da 100%);
  }
  .post--podcast .post__photo {
    background: linear-gradient(100deg, #d8b6a6 0%, #c79c8a 32%, #a486e8 55%, #c8a699 80%, #e4e2ec 100%);
  }

  .post__tear { position: absolute; left: 0; top: 0; width: 493px; height: 493px; }

  .brand {
    position: absolute; right: 9px;
    text-align: right; color: var(--ink); font-weight: 500;
  }
  .post--blog .brand { top: 292px; }
  .post--podcast .brand { top: 284px; }
  .brand__name { display: block; font-size: 22px; letter-spacing: -0.4px; line-height: 1; }
  .brand__sub { display: block; font-size: 7px; letter-spacing: 4px; margin-top: 6px; margin-right: -4px; }

  .title-line {
    position: absolute; right: 9px;
    line-height: 1; white-space: nowrap; text-transform: uppercase;
  }
  .title-line--red { color: var(--red); font-weight: 400; }
  .title-line--ink { color: var(--ink); font-weight: 600; }

  .post--blog .line-1 { top: 352px; font-size: 28px; letter-spacing: 0.2px; }
  .post--blog .line-2 { top: 378px; font-size: 36px; }
  .post--blog .line-3 { top: 411px; font-size: 50px; }

  .post--podcast .line-1 { top: 344px; font-size: 43px; }
  .post--podcast .line-2 { top: 383px; font-size: 63px; }
  .post--podcast .line-3 { top: 443px; font-size: 16px; font-weight: 500; letter-spacing: 0.4px; }
</style>
</head>
<body>

<section class="post post--blog">
  <div class="post__photo" role="img" aria-label="Foto: antiek zakhorloge met ketting op een handgeschreven brief"></div>
  <svg class="post__tear" viewBox="0 0 493 493" aria-hidden="true">
    <polygon fill="var(--kraft)" points="0,470 22,462 40,466 58,462 52,493 0,493"/>
    <polygon fill="var(--kraft)" points="493,124 480,140 468,150 455,170 438,180 424,200 450,194 493,168"/>
    <polygon fill="var(--white)" points="46,493 50,478 57,466 70,455 81,443 98,440 113,433 122,410 136,377 150,370 169,359 200,350 230,340 262,330 290,317 312,302 337,289 355,272 374,256 398,236 421,210 436,204 453,191 472,180 493,163 493,493"/>
  </svg>
  <div class="brand">
    <span class="brand__name">Brightmoor</span>
    <span class="brand__sub">ACADEMY</span>
  </div>
  <div class="title-line title-line--red line-1">Goede voornemens</div>
  <div class="title-line title-line--ink line-2">Die jevolhoudt</div>
  <div class="title-line title-line--ink line-3">-3 tips</div>
</section>

<section class="post post--podcast">
  <div class="post__photo" role="img" aria-label="Foto: twee presentatoren met koptelefoons in de radiostudio"></div>
  <svg class="post__tear" viewBox="0 0 493 493" aria-hidden="true">
    <polygon fill="var(--kraft)" points="0,470 24,462 44,466 60,460 56,493 0,493"/>
    <polygon fill="var(--kraft)" points="493,124 480,142 466,152 452,172 436,182 426,196 452,190 493,168"/>
    <polygon fill="var(--white)" points="51,493 58,476 70,460 90,440 108,420 122,395 136,373 160,362 183,350 215,340 250,326 295,312 318,285 342,256 362,238 384,219 405,205 430,191 460,176 493,158 493,493"/>
  </svg>
  <div class="brand">
    <span class="brand__name">Brightmoor</span>
    <span class="brand__sub">ACADEMY</span>
  </div>
  <div class="title-line title-line--red line-1">Wissel je</div>
  <div class="title-line title-line--ink line-2">Blik</div>
  <div class="title-line title-line--ink line-3">Joris van Elst &amp; Berend</div>
</section>

</body>
</html>
```